Quellora business card design

create modern and tech looking business card that is clean but effectively communciates that we are a cloud communications company.
Should have at minimum:
Employee Name
Postion
Phone Number
Email
website
Contact Information for Business Card
create modern and tech looking business card that is clean but effectively communciates that we are a cloud communications company. We have two logo color schemes (attached) so would like to see designs both ways
Should have at minimum:
Employee Name
Postion
Phone Number
Email
website

```html
<!DOCTYPE html>
<html lang="en">
<head>
<meta charset="utf-8">
<title>Quellora business card</title>
<link rel="stylesheet" href="https://fonts.googleapis.com/css2?family=Open+Sans:wght@400;600;700&display=swap">
<style>
  :root {
    --stage: #3a332f;
    --card: #121214;
    --card-edge: #1d1d20;
    --silver: #9a9a9e;
    --muted: #6f6f74;
    --white: #f4f4f6;
    --purple: #7a3fa3;
    --cyan: #3cbfd8;
    --rule: #8a8a90;
  }
  * { box-sizing: border-box; margin: 0; padding: 0; }
  html, body { width: 1200px; height: 864px; overflow: hidden; }
  body {
    background: var(--stage);
    font-family: "Open Sans", Arial, sans-serif;
    position: relative;
  }
  .card {
    position: absolute;
    width: 680px;
    height: 389px;
    background: var(--card);
    border: 1px solid var(--card-edge);
    border-radius: 4px;
    box-shadow: 0 10px 28px rgba(0,0,0,.45);
  }
  .card--back { left: 70px; top: 30px; }
  .card--front { left: 450px; top: 445px; }

  /* back */
  .back-brand {
    position: absolute;
    left: 0; right: 0; top: 140px;
    display: flex; align-items: center; justify-content: center; gap: 18px;
  }
  .brand-mark { width: 34px; height: 34px; }
  .back-brand .brand-name {
    font-size: 62px; font-weight: 700; letter-spacing: 2px;
    color: var(--silver); text-transform: uppercase;
  }
  .back-web {
    position: absolute; left: 0; right: 0; top: 262px;
    text-align: center; font-size: 15px; letter-spacing: 6px; color: var(--muted);
  }

  /* front */
  .front-brand {
    position: absolute; right: 48px; top: 118px;
    display: flex; align-items: center; gap: 14px;
  }
  .front-brand .brand-name {
    font-size: 46px; font-weight: 700; letter-spacing: 2px;
    color: var(--white); text-transform: uppercase;
  }
  .person { position: absolute; left: 40px; top: 150px; }
  .person-name { color: var(--purple); font-size: 17px; font-weight: 600; text-transform: uppercase; line-height: 1.2; }
  .person-role { color: var(--cyan); font-size: 17px; font-weight: 400; text-transform: uppercase; line-height: 1.3; }
  .rule {
    position: absolute; left: 40px; right: 40px; top: 203px;
    height: 1px; background: var(--rule);
  }
  .contacts { position: absolute; left: 40px; top: 218px; list-style: none; }
  .contacts li {
    display: flex; align-items: center; gap: 12px;
    color: var(--white); font-size: 16px; line-height: 28px;
  }
  .contacts svg { width: 14px; height: 14px; fill: var(--purple); flex: none; }
</style>
</head>
<body>
  <section class="card card--back" aria-label="Card back">
    <div class="back-brand">
      <svg class="brand-mark" viewBox="0 0 10 10" aria-hidden="true"><rect width="10" height="10" fill="#9a9a9e"/></svg>
      <span class="brand-name">Quellora</span>
    </div>
    <p class="back-web">www.quellora.com</p>
  </section>

  <section class="card card--front" aria-label="Card front">
    <div class="front-brand">
      <svg class="brand-mark" viewBox="0 0 10 10" aria-hidden="true"><rect width="10" height="10" fill="#3cbfd8"/></svg>
      <span class="brand-name">Quellora</span>
    </div>
    <div class="person">
      <p class="person-name">Mara Ellison</p>
      <p class="person-role">CEO/Founder</p>
    </div>
    <div class="rule"></div>
    <ul class="contacts">
      <li>
        <svg viewBox="0 0 24 24" aria-hidden="true"><path d="M6.6 10.8a15 15 0 0 0 6.6 6.6l2.2-2.2a1 1 0 0 1 1-.25 11.4 11.4 0 0 0 3.6.57 1 1 0 0 1 1 1V20a1 1 0 0 1-1 1A17 17 0 0 1 3 4a1 1 0 0 1 1-1h3.5a1 1 0 0 1 1 1c0 1.25.2 2.45.57 3.57a1 1 0 0 1-.25 1z"/></svg>
        555 210 4876
      </li>
      <li>
        <svg viewBox="0 0 24 24" aria-hidden="true"><path d="M2 5h20v14H2z M2 5l10 8 10-8" /></svg>
        mara@quellora.com
      </li>
      <li>
        <svg viewBox="0 0 24 24" aria-hidden="true"><path d="M12 2a7 7 0 0 0-7 7c0 5.2 7 13 7 13s7-7.8 7-13a7 7 0 0 0-7-7zm0 9.5A2.5 2.5 0 1 1 12 6.5a2.5 2.5 0 0 1 0 5z"/></svg>
        www.quellora.com
      </li>
    </ul>
  </section>
</body>
</html>
```